NestLoop Landing Page

We need to freshen up our homepage.

The company is NestLoop.com. We provide cloud-based management software for class venues - dance, yoga, martial arts, etc.

The challenge here is to create something that's simultaneously lighthearted and professional. We want our customers to know that the software is easy, fun and non-intimidating, but also powerful enough to handle whatever they throw at it.

Page content can remain the same as it is now. Feel free to move things around, manipulate it however you like.

We like our logo, but feel free to manipulate it as part of your design. Fonts used in the logo are Futura Extra Bold and Rockwell.

NOTE: The default screenshot in the homepage video is NOT our branding choice, it just happens to be the default freeze frame from vidstream.. Feel free to ignore it altogether in your design. We are not affiliated with that character, or the app that we used to create the vid.

Reason: We are extending this contest by request. Out of 65 designs, so far we only really like 4. There's still a good chance to win this contract! Please submit your very best :) Dale

Target Market(s)

Studio owners who are not necessarily tech savvy.

Industry/Entity Type

Software

Requirements
Must have
• Look and feel of a modern web app.

Delivery in a layered PSD.

```html
<!DOCTYPE html>
<html lang="en">
<head>
<meta charset="utf-8">
<title>NestLoop – Class Management Software</title>
<link href="https://fonts.googleapis.com/css2?family=Arvo:wght@400;700&family=Open+Sans:wght@400;600;700&family=Questrial&display=swap" rel="stylesheet">
<style>
:root{
  --navy:#284a72;
  --blue:#6180ad;
  --blue-dark:#3b5b8c;
  --ink:#1f2d44;
  --green:#66d313;
  --green-dark:#3f8c08;
  --orange:#f7941d;
  --orange-light:#ffb347;
  --sky-top:#e3ebf5;
  --sky-bottom:#c6d4e6;
  --white:#ffffff;
  --grey:#5a5a5a;
  --rule:#cfd6e0;
}
*{box-sizing:border-box;margin:0;padding:0}
html,body{width:1004px;height:1200px;overflow:hidden}
body{position:relative;background:var(--white);font-family:"Questrial",sans-serif;color:var(--ink)}
.abs{position:absolute}

/* header */
.site-header{left:0;top:0;width:1004px;height:53px;background:var(--white)}
.brand{left:157px;top:12px;font-family:"Open Sans",sans-serif;font-weight:700;font-size:27px;color:var(--blue-dark);letter-spacing:-0.5px}
.main-nav a{position:absolute;top:0;height:40px;display:flex;align-items:center;justify-content:center;text-align:center;
  font-family:"Open Sans",sans-serif;font-weight:700;font-size:8.5px;line-height:10px;color:var(--white);text-decoration:none;
  background:var(--blue);border-radius:0 0 3px 3px}
.main-nav a.is-active{background:var(--green)}

/* hero */
.hero{left:0;top:53px;width:1004px;height:352px;background:radial-gradient(ellipse at 35% 45%,#f1f5fa 0%,var(--sky-top) 40%,var(--sky-bottom) 100%);overflow:hidden}
.hero-cloud{background:var(--white);border-radius:50%;opacity:.85}
.hero-title{left:156px;top:70px;font-size:20px;line-height:25px;color:var(--ink)}
.hero-sub{left:156px;top:122px;width:330px;font-family:"Open Sans",sans-serif;font-size:13.5px;line-height:17px;color:var(--ink)}
.btn-setup{left:156px;top:169px;width:221px;height:52px;border-radius:26px;background:linear-gradient(var(--orange-light),var(--orange));
  box-shadow:0 3px 0 #b46a12;color:var(--white);text-align:center;font-family:"Open Sans",sans-serif}
.btn-setup strong{display:block;margin-top:11px;font-size:15px}
.btn-setup span{display:block;font-size:10.5px;font-weight:600}
.btn-green{background:var(--green);color:var(--white);font-family:"Open Sans",sans-serif;font-weight:600;text-align:center;border-radius:14px;box-shadow:0 2px 0 var(--green-dark)}
.hero-cta{left:156px;top:235px;width:110px;height:27px;line-height:27px;font-size:11.5px}
.slider-arrow{font-family:"Open Sans",sans-serif;font-size:26px;color:#9aa6b5;font-weight:700}
.photo-cloud{left:500px;top:30px;width:350px;height:280px}
.photo-caption{left:500px;top:246px;width:152px;text-align:right;font-size:12px;line-height:14px;color:var(--ink)}

/* categories */
.category{width:82px;height:82px;border-radius:50%;background:var(--white);border:2px solid var(--blue);text-align:center;
  font-family:"Open Sans",sans-serif;font-size:8px;color:var(--blue)}
.category.is-active{background:var(--blue);border-color:var(--white);color:var(--white)}
.category .icon{width:24px;height:28px;margin:14px auto 8px;border-radius:5px;background:currentColor;opacity:.85}

/* intro */
.intro-band{left:0;top:405px;width:1004px;height:585px;background:var(--blue);border-top:2px solid var(--navy)}
.section-title{font-family:"Arvo",serif;color:var(--white);font-size:20px}
.intro-title{left:157px;top:500px}
.intro-rule{left:157px;top:535px;width:387px;height:1px;background:#c7d3e4}
.intro-text{left:157px;top:547px;width:390px;font-size:11.5px;line-height:15px;color:var(--white)}

/* packages */
.packages{left:157px;top:627px;width:389px;height:291px;background:var(--white);box-shadow:0 1px 3px rgba(0,0,0,.25)}
.tab{position:absolute;top:0;height:33px;line-height:33px;text-align:center;font-size:14.5px;color:var(--white);background:var(--green)}
.tab.is-active{background:var(--white);color:var(--blue-dark)}
.package-title{left:33px;top:51px;font-size:24px;color:var(--blue-dark)}
.feature-col{position:absolute;top:88px;width:152px;list-style:none;font-family:Arial,sans-serif;font-size:10px;color:var(--grey)}
.feature-col li{height:25px;padding-top:3px;border-bottom:1px dashed #c8c8c8}
.ask-row{left:0;top:226px;width:389px;height:22px;border-top:1px solid var(--rule);border-bottom:1px solid var(--rule);
  display:flex;align-items:center;gap:6px;padding-left:31px;font-family:"Open Sans",sans-serif;font-size:12px;color:var(--navy)}
.ask-row b{font-family:"Arvo",serif;font-size:11.5px}
.ask-row .mail{color:var(--orange)}
.ask-row .call{margin-left:6px}
.btn-circle{left:311px;top:884px;width:80px;height:80px;border-radius:50%;background:linear-gradient(var(--orange-light),var(--orange));
  box-shadow:0 3px 0 #b46a12;color:var(--white);font-family:"Arvo",serif;font-size:12px;line-height:15px;text-align:center;padding-top:25px}

/* why card */
.why-card{left:574px;top:502px;width:274px;height:420px;background:var(--white);box-shadow:0 1px 3px rgba(0,0,0,.25);text-align:center}
.why-title{position:absolute;left:0;top:30px;width:100%;font-family:"Arvo",serif;font-size:21px;color:var(--blue)}
.why-rule{position:absolute;left:13px;top:65px;width:250px;height:1px;background:var(--rule)}
.why-list{position:absolute;left:13px;top:77px;width:250px;list-style:none;font-size:13px;color:#666}
.why-list li{height:30px;line-height:30px;border-bottom:1px solid #eef0f3}
.why-list li:last-child{border:none}
.why-list b{font-family:"Open Sans",sans-serif;font-weight:700;font-size:14px;color:#555}
.learn-more{position:absolute;left:105px;top:269px;width:66px;height:16px;line-height:16px;font-size:7px;border-radius:8px}
.social{position:absolute;top:326px;width:46px;height:46px;border-radius:50%;background:var(--navy)}

/* footer */
.site-footer{left:0;top:990px;width:1004px;height:210px;background:var(--navy);color:var(--white)}
.footer-links{left:157px;top:56px;display:flex;gap:8px;font-family:"Open Sans",sans-serif;font-size:10.5px}
.footer-links a{color:var(--white);text-decoration:none}
.footer-rule{left:157px;top:78px;width:327px;height:1px;background:#5a7aa5}
.newsletter-title{left:155px;top:81px;font-family:"Open Sans",sans-serif;font-weight:700;font-size:13px}
.email-field{left:156px;top:102px;width:166px;height:24px;background:var(--white);font-family:"Open Sans",sans-serif;font-size:8.5px;color:#555;padding:8px 9px}
.newsletter-btn{left:154px;top:135px;width:110px;height:25px;line-height:25px;font-size:11.5px}
.footer-brand{left:740px;top:54px;font-family:"Open Sans",sans-serif;font-weight:700;font-size:30px}
.copyright{left:744px;top:125px;font-family:"Open Sans",sans-serif;font-size:10.5px;line-height:12px}
</style>
</head>
<body>

<header class="site-header abs">
  <div class="brand abs">NestLoop</div>
  <nav class="main-nav">
    <a class="is-active" href="#" style="left:634px;width:52px">HOME</a>
    <a href="#" style="left:688px;width:53px">LOGIN</a>
    <a href="#" style="left:743px;width:51px">HELP</a>
    <a href="#" style="left:796px;width:52px">GET<br>STARTED</a>
  </nav>
</header>

<section class="hero abs">
  <div class="hero-cloud abs" style="left:60px;top:45px;width:110px;height:40px"></div>
  <div class="hero-cloud abs" style="left:325px;top:30px;width:50px;height:30px"></div>
  <div class="hero-cloud abs" style="left:775px;top:20px;width:70px;height:35px"></div>
  <div class="hero-cloud abs" style="left:900px;top:-20px;width:110px;height:50px"></div>

  <h1 class="hero-title abs" style="font-weight:400">The Easiest Way to Manage Your<br>Classes and Accept Payments Online.</h1>
  <p class="hero-sub abs">We provide cloud-based management software for class venues dance, yoga, martial arts, etc</p>
  <a class="btn-setup abs"><strong>5 MINUTE SETUP!</strong><span>ITS FREE</span></a>
  <a class="btn-green hero-cta abs">GET STARTED</a>

  <div class="slider-arrow abs" style="left:470px;top:175px">&#8249;</div>
  <div class="slider-arrow abs" style="left:867px;top:175px">&#8250;</div>

  <svg class="photo-cloud abs" viewBox="0 0 350 280" role="img" aria-label="Photo of dancers practising in a studio, framed in a cloud shape">
    <defs>
      <linearGradient id="studio" x1="0" y1="0" x2="0" y2="1">
        <stop offset="0" stop-color="#d9d4cb"/>
        <stop offset=".6" stop-color="#8d867c"/>
        <stop offset="1" stop-color="#4f4b46"/>
      </linearGradient>
    </defs>
    <path d="M70 200 C20 200 0 160 10 130 C20 100 50 95 60 100 C55 70 75 55 105 60 C120 15 180 -5 220 20 C260 10 300 40 295 90 C330 100 350 140 330 175 C315 200 290 205 280 205 C285 250 250 280 215 275 C180 275 165 250 165 235 L165 200 Z" fill="url(#studio)" stroke="var(--white)" stroke-width="3"/>
  </svg>
  <p class="photo-caption abs">Cloud Based<br>Management Software</p>
</section>

<section class="intro-band abs"></section>

<div class="category is-active abs" style="left:497px;top:368px"><div class="icon" role="img" aria-label="Dancer pictogram"></div>DANCE</div>
<div class="category abs" style="left:587px;top:368px"><div class="icon" role="img" aria-label="Yoga pose pictogram"></div>YOGA</div>
<div class="category abs" style="left:676px;top:368px"><div class="icon" role="img" aria-label="Musician pictogram"></div>MUSIC</div>
<div class="category abs" style="left:765px;top:368px"><div class="icon" role="img" aria-label="Martial artist pictogram"></div>MARTIAL ART</div>

<h2 class="section-title intro-title abs" style="font-weight:400">What is NestLoop?</h2>
<div class="intro-rule abs"></div>
<p class="intro-text abs">NestLoop is the easiest and most affordable way to manage your class studio or venue. We help simplify your daily tasks by leveraging the power of the internet, saving you time and money. Anyone can learn to use NestLoop with our clean, common-sense website.</p>

<section class="packages abs">
  <div class="tab is-active" style="left:0;width:125px">Standard</div>
  <div class="tab" style="left:125px;width:122px">Premium</div>
  <div class="tab" style="left:249px;width:140px">Professional</div>
  <h3 class="package-title abs" style="font-weight:400">Free! Standard Package</h3>
  <ul class="feature-col" style="left:33px">
    <li>Fully functional scheduling tool</li><li>Filters for easy viewing</li><li>Track students &amp; instructors</li><li>Store/access Customer Info</li><li style="border:none">Notekeeping &amp; Attendance...</li>
  </ul>
  <ul class="feature-col" style="left:205px">
    <li>Fully functional scheduling tool</li><li>Filters for easy viewing</li><li>Track students &amp; instructors</li><li>Store/access Customer Info</li><li style="border:none">Notekeeping &amp; Attendance...</li>
  </ul>
  <div class="ask-row abs"><b>ASK FOR FREE</b><span class="mail">info@nestloop.com</span><span class="call">Call : 1800 - 555 - 019</span></div>
</section>
<a class="btn-circle abs">GET<br>STARTED</a>

<aside class="why-card abs">
  <h2 class="why-title" style="font-weight:400">What is NestLoop?</h2>
  <div class="why-rule"></div>
  <ul class="why-list">
    <li><b>Web Based</b> - login anywhere</li>
    <li><b>Intuitive</b> - easy to use</li>
    <li><b>Robust</b> - fast and powerful</li>
    <li><b>Secure</b> - your info is super safe</li>
    <li><b>Versatile</b> - suitable for any class venue</li>
    <li><b>Affordable</b> - free version</li>
  </ul>
  <a class="btn-green learn-more">LEARN MORE</a>
  <span class="social" style="left:47px"></span>
  <span class="social" style="left:120px"></span>
  <span class="social" style="left:193px"></span>
</aside>

<footer class="site-footer abs">
  <nav class="footer-links abs">
    <a href="#">About</a><a href="#">Team</a><a href="#">FAQ</a><a href="#">Contact</a><a href="#">Upcoming</a><a href="#">Videos</a><a href="#">Affiliates</a>
  </nav>
  <div class="footer-rule abs"></div>
  <div class="newsletter-title abs">Free Newsletter</div>
  <div class="email-field abs">Email Id</div>
  <a class="btn-green newsletter-btn abs">GET STARTED</a>
  <div class="footer-brand abs">NestLoop</div>
  <p class="copyright abs">© Copyright 2014<br>Terms and Conditions</p>
</footer>

</body>
</html>
```